Billboard for personal injury chiropractors office

We are a personal injury chiropractor clinic.
I need a Billboard with the company name as the dominating factor. Also a smaller picture or 2 of something creative, like a car accident or an arm in a cast off to the sides.
We Like something Clean and Simple and Eye Catching. Please make the picture Small and Off To The Side. The MAIN FOCUS areas are the… name Varden Chiropractic Clinic
At the top CAR ACCIDENT INJURY?
AND at the bottom our number 418-27-FLEXA.
Dr.Milo R. Varden in bold somewhere with the word chiropractor under the doctors name in a text.

Im open to red lettering on white backgrounds, red on yellow backgrounds and I'm also open to reds blues white and yellow. I'd prefer yellow if used be across the bottom.

I am uploading a very rough draft of what we are after along with a screenshot of the tv commercial showing the yellow

DO NOT USE THE LOGO ON THE COMMERCIAL. I JUST WANT THE NAME TYPED LIKE ON SAMPLE BILLBOARD.

Industry/Entity Type

Chiropractic

Colors
0054AA
0677BA
7BADD7
CADEEF
E8F1F8
FFF300
FFF600
FEFA6F
FFFEC7
FFFEE8
EB3D1F
EC4F4E
F09395
F8D3D4
FCEDEE

Requirements
Must have
• Eye catching ,bold

```html
<!DOCTYPE html>
<html lang="en">
<head>
<meta charset="utf-8">
<title>Varden Chiropractic Clinic – Billboard</title>
<link rel="stylesheet" href="https://fonts.googleapis.com/css2?family=Oswald:wght@500;600;700&family=Montserrat:wght@800&display=swap">
<style>
  :root {
    --canvas-bg: #e8e8e8;
    --navy: #1b3577;
    --navy-dark: #142a63;
    --red: #d0121b;
    --yellow: #fff200;
    --white: #ffffff;
    --photo-teal: #1f5a55;
    --photo-light: #d9d4cf;
    --car-dark: #1a1d24;
    --car-mid: #4a4f5a;
  }
  html, body {
    margin: 0;
    padding: 0;
    width: 1023px;
    height: 1200px;
    overflow: hidden;
    background: var(--canvas-bg);
  }
  .canvas {
    position: relative;
    width: 1023px;
    height: 1200px;
    display: flex;
    align-items: center;
    justify-content: center;
  }
  .billboard {
    width: 983px;
    height: auto;
    display: block;
    box-shadow: 0 10px 22px rgba(0,0,0,0.18);
  }
  .headline {
    font-family: "Oswald", "Arial Narrow", sans-serif;
    font-weight: 700;
    paint-order: stroke;
    stroke-linejoin: round;
  }
  .headline--question { fill: var(--red); stroke: var(--yellow); stroke-width: 9px; }
  .headline--clinic { fill: var(--white); stroke: var(--navy-dark); stroke-width: 12px; }
  .tag { font-family: "Oswald", "Arial Narrow", sans-serif; }
  .tag--consult { fill: var(--navy); font-weight: 600; font-size: 25px; }
  .tag--doctor { fill: var(--red); font-weight: 600; font-size: 29px; }
  .phone-number {
    font-family: "Montserrat", Arial, sans-serif;
    font-weight: 800;
    font-size: 68px;
    fill: var(--yellow);
  }
</style>
</head>
<body>
<main class="canvas">
  <svg class="billboard" viewBox="0 0 1140 330" xmlns="http://www.w3.org/2000/svg" aria-label="Varden Chiropractic Clinic billboard">
    <defs>
      <linearGradient id="castPhotoTone" x1="0" y1="0" x2="1" y2="1">
        <stop offset="0" stop-color="var(--photo-teal)"/>
        <stop offset="0.6" stop-color="#2b6660"/>
        <stop offset="1" stop-color="var(--photo-light)"/>
      </linearGradient>
      <linearGradient id="carPhotoTone" x1="0" y1="0" x2="1" y2="1">
        <stop offset="0" stop-color="var(--car-mid)"/>
        <stop offset="0.5" stop-color="var(--car-dark)"/>
        <stop offset="1" stop-color="#2c313b"/>
      </linearGradient>
    </defs>

    <!-- base panel -->
    <rect class="panel" width="1140" height="330" fill="var(--navy)"/>

    <!-- left photo area -->
    <polygon points="0,0 60,0 165,200 165,330 0,330" fill="url(#castPhotoTone)" role="img" aria-label="Photo of a person in green scrubs holding an arm in a white cast"/>
    <!-- red diagonal stripe -->
    <polygon points="60,0 95,0 200,200 165,200" fill="var(--red)"/>

    <!-- red bottom band -->
    <polygon points="215,240 1140,240 1140,330 170,330 200,265" fill="var(--red)"/>
    <!-- white chevron -->
    <polygon points="165,200 185,200 215,265 185,330 165,330 195,265" fill="var(--white)"/>

    <!-- top-right corner accents -->
    <polygon points="1070,0 1140,0 1140,120" fill="var(--red)"/>
    <polygon points="1100,0 1140,0 1140,70" fill="var(--white)"/>

    <!-- right car photo -->
    <polygon points="1080,40 1140,30 1140,330 900,330 860,250 900,190 1000,170" fill="url(#carPhotoTone)" role="img" aria-label="Photo of a black car with a crushed front end after an accident"/>

    <!-- headlines -->
    <text class="headline headline--question" x="600" y="96" text-anchor="middle" font-size="94" textLength="845" lengthAdjust="spacingAndGlyphs">CAR ACCIDENT INJURY?</text>
    <text class="headline headline--clinic" x="600" y="195" text-anchor="middle" font-size="94" textLength="1020" lengthAdjust="spacingAndGlyphs">VARDEN CHIROPRACTIC CLINIC</text>

    <!-- tags -->
    <rect x="285" y="211" width="204" height="42" fill="var(--white)"/>
    <text class="tag tag--consult" x="387" y="242" text-anchor="middle" textLength="188" lengthAdjust="spacingAndGlyphs">FREE CONSULTATION</text>
    <rect x="489" y="211" width="312" height="42" fill="var(--yellow)"/>
    <text class="tag tag--doctor" x="645" y="243" text-anchor="middle" textLength="290" lengthAdjust="spacingAndGlyphs">DR.MILO R.VARDEN,D.C</text>

    <!-- phone -->
    <g class="phone-icon" fill="var(--yellow)" stroke="var(--yellow)" stroke-linecap="round">
      <path d="M252,268 q-8,6 -6,18 q6,20 26,32 q10,5 16,-2 l6,-7 q2,-4 -2,-7 l-9,-7 q-4,-2 -7,1 l-4,4 q-8,-4 -13,-13 l4,-4 q3,-3 1,-7 l-6,-9 q-3,-4 -6,1 z" stroke="none"/>
      <path d="M276,272 a12,12 0 0 1 12,12" fill="none" stroke-width="5"/>
      <path d="M277,260 a24,24 0 0 1 24,24" fill="none" stroke-width="5"/>
    </g>
    <text class="phone-number" x="325" y="318" textLength="530" lengthAdjust="spacingAndGlyphs">418-27-FLEXA</text>
  </svg>
</main>
</body>
</html>
```